Aerospace Private Equity Firm Needs Website

We need a website for new private equity fund called Corvin Partners. We buy smaller companies in the aerospace and industrial industries. I have attached some information about the firm. An example of a site we like that is a similar business but focused in a different sector is www.tarnowcare.com. www.quillstonefunds.com is a firm that also invests in aerospace companies.

Industry/Entity Type

Equity

Number of Pages Required

1 page

Colors
0555a3
33a6d7
ec1f27

```html
<!DOCTYPE html>
<html lang="en">
<head>
<meta charset="utf-8">
<title>Corvin Partners</title>
<link href="https://fonts.googleapis.com/css2?family=Open+Sans:wght@400;600;700&family=Roboto:wght@300;400;500&display=swap" rel="stylesheet">
<style>
:root{
  --navy:#0a3a8a;
  --navy-deep:#062d70;
  --red:#e31e24;
  --red-dark:#b3070d;
  --ink:#333;
  --muted:#666;
  --light:#f4f4f4;
  --white:#fff;
}
*{margin:0;padding:0;box-sizing:border-box}
html,body{width:1200px;height:3651px;overflow:hidden}
body{position:relative;font-family:"Open Sans",sans-serif;color:var(--ink);background:var(--white)}
section,header,footer{position:absolute;left:0;width:1200px}
.abs{position:absolute}
h2{font-family:"Roboto",sans-serif;font-weight:400}
.accent{color:var(--red)}
.btn{position:absolute;height:63px;border-radius:32px;background:var(--red);color:var(--white);font-size:21px;font-family:"Roboto",sans-serif;display:flex;align-items:center;justify-content:center;text-transform:uppercase}

/* header */
.site-header{top:0;height:134px;background:var(--white)}
.brand{left:78px;top:40px;display:flex;align-items:center;gap:12px;font-family:"Roboto",sans-serif;font-weight:500;font-size:34px;color:var(--navy)}
.brand .dot{width:22px;height:22px;border-radius:50%;background:var(--red)}
.utility{right:60px;top:14px;display:flex;gap:22px;font-size:15px;color:#555;align-items:center}
.utility .sep{width:1px;height:20px;background:#ccc}
.search{width:190px;color:#999;font-style:italic;display:flex;gap:8px;align-items:center}
.main-nav{right:78px;top:82px;display:flex;gap:36px;font-family:"Roboto",sans-serif;font-size:17px;font-weight:500;color:#222;text-transform:uppercase}
.main-nav .current{color:var(--red)}

/* hero */
.hero{top:134px;height:543px;background:radial-gradient(ellipse at 50% 30%,#6f7a86 0%,#3b424a 45%,#15181c 100%)}
.hero-title{top:160px;width:100%;text-align:center;font-family:"Roboto",sans-serif;font-weight:500;font-size:80px;color:var(--white)}
.hero-sub{top:258px;width:100%;text-align:center;font-size:25px;color:var(--white)}
.hero-arrow{top:235px;width:30px;height:60px}

/* welcome */
.welcome{top:677px;height:345px;background:var(--white);text-align:center}
.welcome h2{position:absolute;top:60px;width:100%;font-size:50px;color:var(--navy)}
.welcome p{position:absolute;left:150px;width:900px;font-size:14.5px;line-height:27px;color:var(--muted)}

/* criteria */
.criteria{top:1022px;height:395px;background:linear-gradient(90deg,#ebe9e4 0%,#e4e2dc 55%,#d2d6da 100%)}
.criteria-photo{left:560px;top:0;width:640px;height:395px;background:linear-gradient(100deg,rgba(228,226,220,0) 0%,#b8bfc6 30%,#8d949c 70%,#5e656c 100%)}
.criteria h2{position:absolute;left:78px;top:40px;font-size:46px;color:var(--navy)}
.ticks{position:absolute;left:78px;top:106px;list-style:none}
.ticks li{height:31.5px;display:flex;align-items:center;gap:16px;font-size:15px;color:#333}

/* blue bands */
.band{background:var(--navy);color:var(--white);text-align:center}
.band h2{position:absolute;width:100%;font-size:46px}
.band p{position:absolute;width:100%;font-size:19px}
.notch{position:absolute;left:570px;bottom:-30px;width:0;height:0;border-left:30px solid transparent;border-right:30px solid transparent;border-top:30px solid var(--navy)}
.strategy{top:1417px;height:194px;z-index:2}
.team-band{top:2556px;height:202px;z-index:2}

/* sectors */
.sectors{top:1611px;height:531px;background:var(--white)}
.sector{position:absolute;top:51px;width:506px}
.sector-photo{width:506px;height:273px}
.sector-head{position:absolute;top:180px;left:14px;width:462px;height:95px;background:var(--white);padding:14px 18px}
.sector-head h3{font-family:"Roboto",sans-serif;font-weight:400;font-size:40px;color:var(--red);line-height:44px}
.sector-head p{font-size:15px;color:#333;line-height:22px}
.sector ul{position:absolute;top:303px;left:36px;list-style:none}
.sector li{height:33px;display:flex;align-items:center;gap:20px;font-size:15px;color:#333}

/* why */
.why{top:2142px;height:414px;background:linear-gradient(180deg,#6b7480 0%,#b3825c 38%,#d9833c 52%,#5a3a2c 78%,#2a1f1c 100%);text-align:center}
.why h2{position:absolute;top:62px;width:100%;font-size:46px;color:var(--navy)}
.why p{position:absolute;top:134px;left:180px;width:840px;font-size:19px;line-height:28px;color:var(--white)}

/* team */
.team{top:2758px;height:372px;background:var(--white)}
.member{position:absolute;top:62px;width:260px;height:260px}
.member-photo{position:absolute;inset:14px;border-radius:50%;background:radial-gradient(circle at 50% 40%,#e7e9ec 0%,#c8ccd2 60%,#9aa1aa 100%);overflow:hidden}
.member-label{position:absolute;left:28px;top:158px;width:210px;height:46px;color:var(--white);font-size:19px;font-weight:600;display:flex;align-items:center;justify-content:center;border-radius:0 0 0 40px}

/* partners */
.partners{top:3130px;height:175px;background:#f2f2f2}
.partner{position:absolute;top:39px;width:197px;height:98px;background:var(--white);border:1px solid #ddd;display:flex;align-items:center;justify-content:center}
.partner span{display:block;width:120px;height:30px;border-radius:4px;background:#d5d9e0}

/* footer */
.site-footer{top:3305px;height:280px;background:var(--navy);color:var(--white)}
.footer-brand{left:78px;top:68px;display:flex;align-items:center;gap:12px;font-family:"Roboto",sans-serif;font-weight:500;font-size:32px;color:var(--white)}
.footer-brand .dot{width:20px;height:20px;border-radius:50%;background:var(--white)}
.social{left:124px;top:182px;display:flex;gap:16px}
.social span{width:40px;height:40px;border-radius:50%;background:var(--red)}
.footer-col h4{font-size:15px;font-weight:600;color:var(--red);text-transform:uppercase;margin-bottom:14px}
.sitemap{left:343px;top:30px}
.sitemap li{list-style:none;height:27px;font-size:14px;display:flex;align-items:center;gap:14px}
.contact{left:601px;top:30px;font-size:15px;line-height:22px}
.contact .row{display:flex;gap:16px;margin-bottom:16px}
.newsletter{left:874px;top:30px;width:260px;font-size:14px;line-height:22px}
.newsletter .field{margin-top:14px;height:40px;border:1px solid #8aa0c8;border-radius:20px;padding:0 16px;display:flex;align-items:center;color:#b9c6df;font-style:italic;font-size:14px}
.newsletter .btn{position:relative;margin-top:16px;width:182px;height:50px;font-size:19px}
.legal{top:3585px;height:66px;background:var(--red-dark);color:var(--white);font-size:14px;display:flex;align-items:center;justify-content:center}
</style>
</head>
<body>

<header class="site-header">
  <div class="abs brand"><span class="dot"></span>Corvin Partners</div>
  <div class="abs utility">
    <span>Login</span><span class="sep"></span><span>Register</span><span class="sep"></span>
    <span>Language ▾</span><span class="sep"></span>
    <span class="search"><svg width="14" height="14" viewBox="0 0 14 14"><circle cx="6" cy="6" r="4.5" fill="none" stroke="#e31e24" stroke-width="2"/><line x1="9.5" y1="9.5" x2="13" y2="13" stroke="#e31e24" stroke-width="2"/></svg>Search Here....</span>
  </div>
  <nav class="abs main-nav">
    <span class="current">Home ▾</span><span>Strategy</span><span>Investment</span><span>Team</span><span>Partners</span><span>Case Study</span><span>Contact</span>
  </nav>
</header>

<section class="hero" role="img" aria-label="Aircraft cockpit interior seen from the pilot seat">
  <svg class="abs hero-arrow" style="left:30px" viewBox="0 0 30 60"><polyline points="26,4 6,30 26,56" fill="none" stroke="#fff" stroke-width="2"/></svg>
  <svg class="abs hero-arrow" style="right:30px" viewBox="0 0 30 60"><polyline points="4,4 24,30 4,56" fill="none" stroke="#fff" stroke-width="2"/></svg>
  <div class="abs hero-title">Corvin Partners Fund</div>
  <div class="abs hero-sub">Lower Middle-Market Buyout Fund $200 Million Target, $250 Million Hard Cap.</div>
  <div class="btn" style="left:406px;top:350px;width:183px">Learn More</div>
  <div class="btn" style="left:608px;top:350px;width:185px">Join With Us</div>
</section>

<section class="welcome">
  <h2>Welcome To <span class="accent">Corvin Partners</span></h2>
  <p style="top:130px">Corvin Partners ("Corvin") is a Los Angeles, California-based private equity firm formed in 2016 by Principals from Larchmont Ridge Associates (LRA). Corvin focuses on lower middle-market control investments in aerospace and industrial companies based in North America.</p>
  <p style="top:200px">The Corvin team has invested successfully in these sectors over a 10- year period while at LRA. Founded in 2016 by Principals from Larchmont Ridge Associates (LRA) - Los Angeles, CA Corvin Partners LP: $200 million with hard cap of $250 million Buyout strategy targeting small aerospace &amp; industrial companies in North America.</p>
  <svg class="abs" style="left:590px;top:282px" width="20" height="20" viewBox="0 0 20 20"><polyline points="4,3 10,9 16,3" fill="none" stroke="#e31e24" stroke-width="2"/><polyline points="4,10 10,16 16,10" fill="none" stroke="#e31e24" stroke-width="2"/></svg>
</section>

<section class="criteria">
  <div class="abs criteria-photo" role="img" aria-label="Vintage propeller aircraft flying through a cloudy sky"></div>
  <h2>Investment <span class="accent">Criteria</span></h2>
  <ul class="ticks">
    <li><svg width="14" height="12" viewBox="0 0 14 12"><polyline points="1,6 5,10 13,1" fill="none" stroke="#e31e24" stroke-width="2.4"/></svg>Value focused</li>
    <li><svg width="14" height="12" viewBox="0 0 14 12"><polyline points="1,6 5,10 13,1" fill="none" stroke="#e31e24" stroke-width="2.4"/></svg>Family or entrepreneur-owned / Corporate carve-outs</li>
    <li><svg width="14" height="12" viewBox="0 0 14 12"><polyline points="1,6 5,10 13,1" fill="none" stroke="#e31e24" stroke-width="2.4"/></svg>EBITDA up to $10mm</li>
    <li><svg width="14" height="12" viewBox="0 0 14 12"><polyline points="1,6 5,10 13,1" fill="none" stroke="#e31e24" stroke-width="2.4"/></svg>Enterprise Value $20-$100mm</li>
    <li><svg width="14" height="12" viewBox="0 0 14 12"><polyline points="1,6 5,10 13,1" fill="none" stroke="#e31e24" stroke-width="2.4"/></svg>Deploy $10-$25mm in equity per investment</li>
    <li><svg width="14" height="12" viewBox="0 0 14 12"><polyline points="1,6 5,10 13,1" fill="none" stroke="#e31e24" stroke-width="2.4"/></svg>Profitable, stable, cash-flowing companies</li>
    <li><svg width="14" height="12" viewBox="0 0 14 12"><polyline points="1,6 5,10 13,1" fill="none" stroke="#e31e24" stroke-width="2.4"/></svg>Opportunity for growth, strategic &amp; operational change</li>
    <li><svg width="14" height="12" viewBox="0 0 14 12"><polyline points="1,6 5,10 13,1" fill="none" stroke="#e31e24" stroke-width="2.4"/></svg>Target 70% aerospace / 30% industrial</li>
  </ul>
</section>

<section class="band strategy">
  <h2 style="top:66px">Investment <span class="accent">Strategy</span></h2>
  <p style="top:120px">50,000+ private, small-cap, aerospace &amp; industrial companies</p>
  <span class="notch"></span>
</section>

<section class="sectors">
  <div class="sector" style="left:78px">
    <div class="sector-photo" role="img" aria-label="Nose of a white and blue passenger jet on the apron" style="background:linear-gradient(180deg,#b9c9dc 0%,#e8edf2 45%,#6f88b0 75%,#2c3f66 100%)"></div>
    <div class="sector-head"><h3>Aerospace</h3><p>Deep network of people, companies, resources</p></div>
    <ul>
      <li><svg width="16" height="12" viewBox="0 0 16 12"><polyline points="1,5 6,10 15,1" fill="none" stroke="#e31e24" stroke-width="2.4"/></svg>Metallic Structures</li>
      <li><svg width="16" height="12" viewBox="0 0 16 12"><polyline points="1,5 6,10 15,1" fill="none" stroke="#e31e24" stroke-width="2.4"/></svg>Fluid Conveyance</li>
      <li><svg width="16" height="12" viewBox="0 0 16 12"><polyline points="1,5 6,10 15,1" fill="none" stroke="#e31e24" stroke-width="2.4"/></svg>Composite Structures</li>
      <li><svg width="16" height="12" viewBox="0 0 16 12"><polyline points="1,5 6,10 15,1" fill="none" stroke="#e31e24" stroke-width="2.4"/></svg>Surface Treatment</li>
    </ul>
  </div>
  <div class="sector" style="left:618px">
    <div class="sector-photo" role="img" aria-label="Jet engine on a stand in a maintenance hangar" style="background:linear-gradient(180deg,#c7d3de 0%,#8fa0b0 40%,#4d5a68 75%,#2f3843 100%)"></div>
    <div class="sector-head"><h3>Industrial</h3><p>Companies that share common characteristics with aerospace</p></div>
    <ul>
      <li><svg width="16" height="12" viewBox="0 0 16 12"><polyline points="1,5 6,10 15,1" fill="none" stroke="#e31e24" stroke-width="2.4"/></svg>Regulated quality control</li>
      <li><svg width="16" height="12" viewBox="0 0 16 12"><polyline points="1,5 6,10 15,1" fill="none" stroke="#e31e24" stroke-width="2.4"/></svg>Product certification</li>
      <li><svg width="16" height="12" viewBox="0 0 16 12"><polyline points="1,5 6,10 15,1" fill="none" stroke="#e31e24" stroke-width="2.4"/></svg>Precision manufacturing</li>
      <li><svg width="16" height="12" viewBox="0 0 16 12"><polyline points="1,5 6,10 15,1" fill="none" stroke="#e31e24" stroke-width="2.4"/></svg>Engineering driven</li>
    </ul>
  </div>
</section>

<section class="why" role="img" aria-label="Row of fighter jets on a runway at sunset">
  <h2>Why Best <span class="accent">Corvin Partners</span></h2>
  <p>Smaller companies may not be able to meet the increased financial, program management, skills, risk-taking and investment requirements</p>
  <div class="btn" style="left:507px;top:226px;width:186px">Join With Us</div>
</section>

<section class="band team-band">
  <h2 style="top:52px">Meet Our <span class="accent">Team</span></h2>
  <p style="top:112px">60 years of combined investing and operating experience</p>
  <span class="notch"></span>
</section>

<section class="team">
  <div class="member" style="left:116px">
    <svg class="abs" width="260" height="260" viewBox="0 0 260 260"><path d="M130 6 A124 124 0 0 0 130 254" fill="none" stroke="#0a3a8a" stroke-width="12"/></svg>
    <div class="member-photo" role="img" aria-label="Portrait of a team member in a suit"></div>
    <div class="member-label" style="background:var(--navy)">Member Name</div>
  </div>
  <div class="member" style="left:471px">
    <svg class="abs" width="260" height="260" viewBox="0 0 260 260"><path d="M130 6 A124 124 0 0 0 130 254" fill="none" stroke="#e31e24" stroke-width="12"/></svg>
    <div class="member-photo" role="img" aria-label="Portrait of a team member in a blazer"></div>
    <div class="member-label" style="background:var(--red)">Member Name</div>
  </div>
  <div class="member" style="left:824px">
    <svg class="abs" width="260" height="260" viewBox="0 0 260 260"><path d="M130 6 A124 124 0 0 0 130 254" fill="none" stroke="#0a3a8a" stroke-width="12"/></svg>
    <div class="member-photo" role="img" aria-label="Portrait of a team member in a suit"></div>
    <div class="member-label" style="background:var(--navy)">Member Name</div>
  </div>
</section>

<section class="partners">
  <svg class="abs" style="left:28px;top:68px" width="18" height="40" viewBox="0 0 18 40"><polyline points="16,2 3,20 16,38" fill="none" stroke="#999" stroke-width="2"/></svg>
  <div class="partner" style="left:78px"><span></span></div>
  <div class="partner" style="left:290px"><span></span></div>
  <div class="partner" style="left:501px"><span></span></div>
  <div class="partner" style="left:713px"><span></span></div>
  <div class="partner" style="left:925px"><span></span></div>
  <svg class="abs" style="right:28px;top:68px" width="18" height="40" viewBox="0 0 18 40"><polyline points="2,2 15,20 2,38" fill="none" stroke="#999" stroke-width="2"/></svg>
</section>

<footer class="site-footer">
  <div class="abs footer-brand"><span class="dot"></span>Corvin Partners</div>
  <div class="abs social"><span></span><span></span><span></span></div>
  <div class="abs footer-col sitemap">
    <h4>Sitemap</h4>
    <ul>
      <li><span class="accent">»</span>Home</li><li><span class="accent">»</span>Strategy</li><li><span class="accent">»</span>Investment</li><li><span class="accent">»</span>Team</li><li><span class="accent">»</span>Partners</li><li><span class="accent">»</span>Case Study</li><li><span class="accent">»</span>Contact</li>
    </ul>
  </div>
  <div class="abs footer-col contact">
    <h4>Get In Touch</h4>
    <div class="row"><svg width="18" height="26" viewBox="0 0 18 26"><path d="M9 1a8 8 0 0 0-8 8c0 6 8 16 8 16s8-10 8-16a8 8 0 0 0-8-8z" fill="#e31e24"/><circle cx="9" cy="9" r="3" fill="#0a3a8a"/></svg><div><strong style="font-size:17px;font-weight:600">Corvin Partners</strong><br>4120 Meridian Park Blvd<br>Suite 210<br>Los Angeles, CA 90025</div></div>
    <div class="row"><svg width="18" height="18" viewBox="0 0 18 18"><path d="M4 1l3 4-2 2c1 2 3 4 5 5l2-2 4 3-2 3C8 16 2 10 1 3z" fill="#e31e24"/></svg>(310) 555-0142</div>
    <div class="row"><svg width="18" height="14" viewBox="0 0 18 14"><rect x="1" y="1" width="16" height="12" fill="none" stroke="#e31e24" stroke-width="2"/><polyline points="1,1 9,8 17,1" fill="none" stroke="#e31e24" stroke-width="2"/></svg>info@corvinpartners.com</div>
  </div>
  <div class="abs footer-col newsletter">
    <h4>Newsletter</h4>
    <p>Would you like to receive exclusive access to articles, white papers and our regular monthly newsletter?</p>
    <div class="field">Type Your E-mail</div>
    <div class="btn">Subscribe</div>
  </div>
</footer>
<div class="abs legal" style="left:0;width:1200px">©Corvin Partners - 2017. All Rights Reserved.</div>

</body>
</html>
```